Design an IT/hosting company homepage in Visual Composer (WordPress)

Hi,

we are building our new site. We are looking for a fantastic homepage design.

We don't know what we want exactly on our homepage, so we'll leave it up to your suggestions. What we think that should be there:
- A slider (we want you to create some sample slides as well)
- Our most important services (see below).
- Some images and/or icons
- Some written content
- Call to actions
- ...

The design has to be in line with the branding an other pages we already have in place. It has to be eye catching and contain CTA's.
Our website is created with the Avada theme, and Visual composer is available as well.

Header: [url removed, login to view]
Some example pages:

if you want to see the live website, drop me a message and I'll share the URL.

Following colours are used in our logo:
1: 44A7DE
2: 2194D2
3: 848585
4: 535453

Some info about our company:
• Founded in 2004
• Located in Belgium
• Aiming at private customers & small to mid size companies.
• Pro service at budget price
• Enterprise standards
• On our prio list: 99,9% uptime, fast support, privacy, solid solutions, personal approach
• Fast support via mail, chat & phone, both in Dutch & English
• Team of well-trained engineers
• 1 datacenter in Belgium
• 1 datacenter in Netherlands

Our most important services:

Web hosting starting at €2,5 a month:
• Fast hosting with SSD disks
• Servers in Belgium & Netherlands
• All package include unlimited bandwidth, advanced protection/firewalling, daily backups, and fast support
• Our hosting packages come with a free .be/.nl/.eu/.com domain name, & unlimited email accounts
• When you take a hosting account with us, we provide a free service to move from your old host to us, or we install WordPress, Joomla or Drupal for you

Online Backup
• Backup all your data to the secure cloud
• Recover your data after data loss (crash, theft, fire, …)
• 3 storage options: 5GB, 50GB & unlimited (unlimited is pretty unique)
• Backup of Desk Suite 12 accounts to the secure cloud
• Backups of Norvanta NAS to the secure cloud
• In case of disaster, we can come to your house or office with the backup data
• Starting at 5€ with 5GB storage and €20 with unlimited storage
• No setup costs or fixed contracts. Cancel at any time.
• Free 14 day trial

Virtual Servers start at €10/month:
• Fast SSD VPS servers, based on Quelbix, with premium hardware
• A Virtual Private Server (VPS) is a hosting environment that combines the benefits of shared hosting and dedicated servers.
• Very scalable and flexible. If you need extra resources, these can be added quickly.
• Windows or Linux
• Options available like daily backups (onsite or offsite) or HA setup

Domain names:
• We can register all domain name extensions available
• Realtime registration
• Free 5 GB mailbox and e-mail address
• Free Unlimited number of subdomains
• Free Full control over the DNS settings
• Free Unlimited e-mail aliases for mail forwarding
• Starting at €10/year

Wordpress managed hosting:
• Same as normal hosting, but optimized for Wordpress
• We manage WP for you
• Monthly updates for Wordpress & plugins
• Security hardening

Joomla managed hosting:
• Same as normal hosting, but optimized for Joomla
• We manage Jooma for you
• Monthly updates for Joomla & plugins
• Security hardening

Please submit your mockups & details about your design.
After we choose & award an entry, we'll give you credentials to our website, and you have to create the page as per your entry in WordPress.

Thanks, good luck, and amaze us! :)

```html
<!DOCTYPE html>
<html lang="en">
<head>
<meta charset="utf-8">
<title>Cloudmere – Hosting, Backup &amp; Servers</title>
<link href="https://fonts.googleapis.com/css2?family=Source+Sans+3:wght@300;400;600;700&display=swap" rel="stylesheet">
<style>
  :root {
    --sky: #44a7de;
    --ocean: #2194d2;
    --ocean-band: #2e8ed6;
    --stone: #848585;
    --slate: #535453;
    --ink: #333333;
    --paper: #ffffff;
    --rule: #e4e4e4;
  }
  * { box-sizing: border-box; margin: 0; padding: 0; }
  html, body { width: 780px; height: 1200px; overflow: hidden; }
  body { font-family: "Source Sans 3", Arial, sans-serif; background: var(--paper); color: var(--ink); position: relative; }

  .topbar { position: absolute; left: 0; top: 0; width: 780px; height: 19px; border-top: 2px solid var(--ocean); border-bottom: 1px solid var(--rule); font-size: 5px; color: #777; }
  .topbar .contact { position: absolute; left: 148px; top: 6px; }
  .topbar .links { position: absolute; left: 452px; top: 6px; display: flex; gap: 22px; font-weight: 600; color: #555; }
  .flag { position: absolute; top: 7px; width: 8px; height: 5px; }
  .flag.nl { left: 592px; background: linear-gradient(#c0262d 33%, #fff 33% 66%, #21468b 66%); }
  .flag.en { left: 616px; background: #2a3f8f; }

  .navbar { position: absolute; left: 0; top: 19px; width: 780px; height: 26px; border-bottom: 1px solid #333; }
  .brand { position: absolute; left: 150px; top: 6px; display: flex; align-items: center; gap: 4px; font-size: 11px; font-weight: 600; color: var(--sky); letter-spacing: .5px; }
  .brand .mark { width: 12px; height: 12px; background: var(--sky); }
  .menu { position: absolute; left: 369px; top: 10px; display: flex; gap: 12px; font-size: 5px; font-weight: 700; color: #333; }

  .hero { position: absolute; left: 0; top: 45px; width: 780px; height: 205px; background: radial-gradient(ellipse at 75% 40%, #4a4a4a, #1c1c1c 75%); overflow: hidden; }
  .hero svg { position: absolute; left: 0; top: 0; }
  .hero h1 { position: absolute; right: 54px; top: 30px; text-align: right; color: #fff; font-weight: 400; font-size: 38px; line-height: 44px; }

  .services { position: absolute; left: 0; top: 250px; width: 780px; height: 221px; display: flex; }
  .service { width: 195px; height: 221px; position: relative; color: #fff; text-align: center; }
  .service.hosting { background: var(--sky); }
  .service.backup { background: var(--ocean); }
  .service.vps { background: var(--stone); }
  .service.domains { background: var(--slate); }
  .service svg { position: absolute; left: 69px; top: 50px; }
  .service h2 { position: absolute; left: 0; width: 100%; top: 113px; font-size: 15px; font-weight: 400; }
  .service.vps h2, .service.domains h2 { top: 117px; }
  .btn-outline { display: inline-block; border: 2px solid #fff; color: #fff; font-size: 14px; font-weight: 400; padding: 2px 6px; line-height: 18px; text-decoration: none; }
  .service .btn-outline { position: absolute; top: 144px; left: 50%; transform: translateX(-50%); white-space: nowrap; }

  .backup-feature { position: absolute; left: 0; top: 471px; width: 780px; height: 400px; }
  .backup-feature .screens { position: absolute; left: 22px; top: 71px; width: 334px; height: 256px; background: linear-gradient(135deg, #f3f3f3, #d9d9d9 60%, #bfbfbf); }
  .backup-feature .copy { position: absolute; right: 42px; top: 55px; width: 250px; text-align: right; }
  .backup-feature h3 { color: var(--ocean); font-size: 18px; font-weight: 700; margin-bottom: 14px; }
  .backup-feature .lead { color: var(--ocean); font-size: 14.5px; font-weight: 300; line-height: 17.5px; margin-bottom: 17px; }
  .backup-feature .terms { color: var(--ink); font-size: 14.5px; font-weight: 400; line-height: 17.5px; }

  .vps-feature { position: absolute; left: 0; top: 871px; width: 780px; height: 250px; background: var(--ocean-band); color: #fff; }
  .vps-feature h3 { position: absolute; left: 38px; top: 51px; font-size: 17px; font-weight: 700; line-height: 21px; }
  .vps-feature p { position: absolute; left: 38px; top: 113px; width: 280px; font-size: 14.5px; font-weight: 300; line-height: 17.5px; }
  .vps-feature .btn-outline { position: absolute; left: 38px; top: 182px; }
  .vps-feature .hardware { position: absolute; left: 433px; top: 42px; width: 330px; height: 166px; background: linear-gradient(180deg, #3a3f45, #1b1e22 45%, #2b8bd4 48% 52%, #1b1e22 55%, #3a3f45); }

  .divider { position: absolute; left: 0; top: 1121px; width: 780px; height: 17px; background: #8f8f8f; }
  .cta { position: absolute; left: 0; top: 1138px; width: 780px; height: 62px; background: var(--slate); color: #fff; }
  .cta p { position: absolute; left: 37px; top: 16px; font-size: 18.5px; font-weight: 400; }
  .cta a { position: absolute; left: 583px; top: 15px; width: 155px; height: 26px; background: var(--sky); color: #fff; text-align: center; line-height: 26px; font-size: 15px; text-decoration: none; }
</style>
</head>
<body>

<header>
  <div class="topbar">
    <span class="contact">Contact us! +32 9 000 00 00 | hello@cloudmere.be</span>
    <nav class="links"><span>Client Area</span><span>Status</span><span>Support</span></nav>
    <span class="flag nl"></span><span class="flag en"></span>
  </div>
  <div class="navbar">
    <div class="brand"><span class="mark"></span>CLOUDMERE</div>
    <nav class="menu">
      <span>HOSTING &amp; DOMAINS ▾</span><span>BACKUP ▾</span><span>SERVICES ▾</span><span>SOFTWARE ▾</span><span>ABOUT ▾</span><span>CONTACT</span>
    </nav>
  </div>
</header>

<section class="hero" role="img" aria-label="Dark honeycomb metal texture with silver and blue diagonal bands">
  <svg width="780" height="205" viewBox="0 0 780 205">
    <polygon points="0,0 485,0 395,78 0,78" fill="#bdbdbd"/>
    <polygon points="0,42 430,42 400,68 0,68" fill="#2aa0e0"/>
    <polygon points="0,78 395,78 370,100 0,100" fill="#9a9a9a"/>
    <polygon points="485,0 500,0 410,78 395,78" fill="#e6e6e6"/>
  </svg>
  <h1>Web hosting<br>starting at €2,5<br>a month</h1>
</section>

<section class="services">
  <div class="service hosting">
    <svg width="56" height="56" viewBox="0 0 56 56" fill="none" stroke="#fff" stroke-width="2">
      <circle cx="28" cy="28" r="26"/>
      <path d="M17 30a7 7 0 0 1 2-13 9 9 0 0 1 17-2 7 7 0 0 1 3 14"/>
      <rect x="20" y="22" width="16" height="5"/><rect x="20" y="29" width="16" height="5"/><rect x="20" y="36" width="16" height="5"/>
      <path d="M28 41v5M20 46h16"/>
    </svg>
    <h2>Web Hosting</h2>
    <a class="btn-outline" href="#">Learn More</a>
  </div>
  <div class="service backup">
    <svg width="56" height="56" viewBox="0 0 56 56">
      <circle cx="28" cy="28" r="26" fill="none" stroke="#fff" stroke-width="2"/>
      <path d="M17 36a7 7 0 0 1 1-14 10 10 0 0 1 19-3 8 8 0 0 1 2 17z" fill="#fff"/>
      <path d="M28 33v-9M23 28l5-5 5 5" stroke="#2194d2" stroke-width="3" fill="none"/>
    </svg>
    <h2>Online Backup</h2>
    <a class="btn-outline" href="#">Learn More</a>
  </div>
  <div class="service vps">
    <svg width="56" height="56" viewBox="0 0 56 56" fill="none" stroke="#fff" stroke-width="2">
      <circle cx="28" cy="28" r="26"/>
      <rect x="17" y="14" width="22" height="28"/>
      <path d="M17 21h22M17 28h22M17 35h22M20 17.5h16M20 24.5h16M20 31.5h16M20 38.5h16" stroke-width="1"/>
    </svg>
    <h2>Virtual Serviers</h2>
    <a class="btn-outline" href="#">Learn More</a>
  </div>
  <div class="service domains">
    <svg width="56" height="56" viewBox="0 0 56 56" fill="none" stroke="#fff" stroke-width="2">
      <circle cx="28" cy="28" r="26"/>
      <circle cx="28" cy="28" r="17"/>
      <ellipse cx="28" cy="28" rx="7" ry="17"/>
      <rect x="11" y="22" width="34" height="11" fill="#535453" stroke="none"/>
      <text x="28" y="31.5" text-anchor="middle" fill="#fff" stroke="none" font-size="10" font-weight="700" font-family="Source Sans 3, sans-serif">WWW</text>
    </svg>
    <h2>Domains &amp; Management</h2>
    <a class="btn-outline" href="#">Learn More</a>
  </div>
</section>

<section class="backup-feature">
  <div class="screens" role="img" aria-label="Two desktop monitors showing the dedicated servers page"></div>
  <div class="copy">
    <h3>Online Backup</h3>
    <p class="lead">Backup all your data to the secure cloud and recover your data after data loss (crash, theft, fire, …). There are 3 storage options: 5GB, 50GB &amp; unlimited (unlimited is pretty unique) giving you enough to be able to backup Desk Suite 12 accounts to the secure cloud. In case of disaster, we can come to your house or office with the backup data</p>
    <p class="terms">Starting at 5€ with 5GB storage and €20 with unlimited storage. No setup costs or fixed contracts. Cancel at any time! Try our free 14 day trial</p>
  </div>
</section>

<section class="vps-feature">
  <h3>Fast SSD VPS servers, based on<br>Quelbix, with premium hardware</h3>
  <p>A Virtual Private Server (VPS) is a hosting environment that combines the benefits of shared hosting and dedicated servers.</p>
  <a class="btn-outline" href="#">Learn More</a>
  <div class="hardware" role="img" aria-label="Two rack servers joined by a plus sign"></div>
</section>

<div class="divider"></div>
<section class="cta">
  <p>Get in touch with our expert team to see how we can help you.</p>
  <a href="#">Contact Us</a>
</section>

</body>
</html>
```